" Oferecemos consultoria à empresas de Comércio Exterior. São dois serviços ofertados pela nossa empresa: 1) PMV 716 - auxiliamos empresas de SC a tirar o benefício fiscal. 2) FULCO - auxiliamos empresas de todos os estados brasileiros a tirar o FULCO Expresso de Importação/Exportação "

```html
<!DOCTYPE html>
<html lang="pt-BR">
<head>
<meta charset="UTF-8">
<title>Rota Aduaneira — Consultoria em Comércio Exterior</title>
<link rel="stylesheet" href="https://fonts.googleapis.com/css2?family=Poppins:wght@400;500;600;800&display=swap">
<style>
  :root{
    --page:#eceef1;
    --white:#ffffff;
    --ink:#2a2b2f;
    --muted:#8b8d93;
    --bar:#25262a;
    --red:#e2303f;
    --blue:#2f6fd6;
    --hero-top:#2c3a4a;
    --hero-mid:#6a5a44;
    --hero-low:#1c2530;
  }
  *{box-sizing:border-box;margin:0;padding:0}
  html,body{width:1200px;height:1200px;overflow:hidden}
  body{background:var(--page);font-family:"Poppins",sans-serif;position:relative}

  .screen{
    position:absolute;left:330px;top:40px;width:540px;height:1120px;
    border-radius:56px;overflow:hidden;background:var(--white);
    box-shadow:0 30px 60px rgba(0,0,0,.18);
    display:flex;flex-direction:column;
  }
  .status-bar{height:54px;display:flex;align-items:center;padding:0 44px;
    font-weight:600;font-size:18px;color:var(--ink)}

  .site-header{height:120px;display:flex;flex-direction:column;align-items:center;justify-content:center;gap:4px}
  .brand-name{font-weight:500;font-size:28px;line-height:1.1;color:var(--ink)}
  .brand-tagline{font-size:13px;color:var(--muted)}

  .nav-bar{height:56px;background:var(--bar);display:flex;align-items:center;justify-content:space-between;padding:0 30px}

  .hero{position:relative;flex:1;
    background:linear-gradient(180deg,var(--hero-top) 0%,#4a4d55 30%,var(--hero-mid) 55%,#3b3e44 75%,var(--hero-low) 100%)}
  .hero-photo{position:absolute;inset:0}
  .hero-copy{position:absolute;left:0;right:0;top:410px;text-align:center;color:var(--white)}
  .hero-title{font-weight:800;font-size:44px;line-height:1.08}
  .hero-sub{font-size:21px;line-height:1.3;margin-top:12px;color:#e8e9ec}

  .contact-chip{position:absolute;right:40px;top:640px;display:flex;align-items:center;gap:14px}
  .avatar{width:64px;height:64px;border-radius:50%;background:#b9b3ab;border:4px solid var(--white)}
  .contact-info{display:flex;flex-direction:column;gap:2px}
  .contact-name{font-weight:600;font-size:14px;color:var(--red)}
  .contact-role{font-size:11px;color:#d9dadd}
  .contact-btn{margin-top:4px;background:var(--blue);color:var(--white);font-size:12px;font-weight:500;
    border-radius:12px;padding:3px 14px;text-align:center}

  .action-bar{height:96px;background:var(--bar);display:flex;align-items:center;justify-content:space-between;padding:0 34px}
  .btn-more{background:var(--red);color:var(--white);font-weight:600;font-size:20px;border-radius:26px;padding:10px 44px}
  .btn-watch{display:flex;align-items:center;gap:14px;color:var(--white);font-weight:600;font-size:20px}
</style>
</head>
<body>
  <main class="screen">
    <div class="status-bar">5:20</div>

    <header class="site-header">
      <span class="brand-name">Rota Aduaneira</span>
      <span class="brand-tagline">assessoria internacional</span>
    </header>

    <nav class="nav-bar">
      <svg class="icon-search" width="26" height="26" viewBox="0 0 26 26" aria-label="Buscar">
        <circle cx="11" cy="11" r="7.5" fill="none" stroke="var(--red)" stroke-width="3"/>
        <line x1="16.5" y1="16.5" x2="23" y2="23" stroke="var(--red)" stroke-width="3" stroke-linecap="round"/>
      </svg>
      <svg class="icon-menu" width="34" height="24" viewBox="0 0 34 24" aria-label="Menu">
        <rect x="6" y="2" width="28" height="3.5" fill="#fff"/>
        <rect x="0" y="10" width="34" height="3.5" fill="#fff"/>
        <rect x="12" y="18" width="22" height="3.5" fill="#fff"/>
      </svg>
    </nav>

    <section class="hero">
      <div class="hero-photo" role="img" aria-label="Foto de porto com guindastes e contêineres ao entardecer"></div>
      <div class="hero-copy">
        <h1 class="hero-title">Eleve seus<br>lucros em até 20%</h1>
        <p class="hero-sub">Através da redução da carga<br>tributária da sua empresa</p>
      </div>
      <div class="contact-chip">
        <div class="avatar" role="img" aria-label="Foto do consultor"></div>
        <div class="contact-info">
          <span class="contact-name">Lucas Prado</span>
          <span class="contact-role">Gerente de Vendas</span>
          <span class="contact-btn">Dúvidas?</span>
        </div>
      </div>
    </section>

    <footer class="action-bar">
      <span class="btn-more">Saiba +</span>
      <span class="btn-watch">Assista
        <svg width="30" height="30" viewBox="0 0 30 30" aria-hidden="true">
          <circle cx="15" cy="15" r="13" fill="none" stroke="#fff" stroke-width="2.5"/>
          <path d="M12 9.5 L20.5 15 L12 20.5 Z" fill="#fff"/>
        </svg>
      </span>
    </footer>
  </main>
</body>
</html>
```